Startup of Management Company looking for Designers!

I am looking for an upscale website. Veltrona will focus on Real Estate, Wealth Management, and Consulting,

Target Market(s)

investors, sellers of real estate, people looking to have their real estate management.
companies looking for consulting services

Number of Pages Required

5+ page

Font styles to use
Sans Serif

Requirements
Must have
• pictures, real.

```html
<!DOCTYPE html>
<html lang="en">
<head>
<meta charset="utf-8">
<title>Veltrona – Business and Consulting Services</title>
<link href="https://fonts.googleapis.com/css2?family=Montserrat:wght@400;500;600;700&display=swap" rel="stylesheet">
<style>
:root{
  --navy:#1b2a6b;
  --red:#d0111b;
  --orange:#f59a00;
  --ink:#222;
  --light:#f2f2f2;
  --line:#e3e3e3;
  --white:#fff;
}
*{margin:0;padding:0;box-sizing:border-box}
html,body{width:1200px;height:2798px;overflow:hidden}
body{position:relative;background:var(--white);font-family:"Montserrat",sans-serif;color:var(--ink)}
.abs{position:absolute}
.logo{left:163px;top:28px;font-size:28px;font-weight:700;color:var(--navy);letter-spacing:.5px}
.nav{top:37px;font-size:13px;color:var(--ink);text-transform:uppercase}
.nav.active{color:var(--navy);font-weight:600}
.hero{left:0;top:86px;width:1072px;height:509px;background:linear-gradient(120deg,#3a4a7e 0%,#6f82ad 45%,#8a9bbf 60%,#2a3869 100%)}
.hero-title{left:0;top:340px;width:1072px;text-align:center;color:var(--white);font-size:43px;font-weight:700;line-height:50px;text-shadow:0 2px 4px rgba(0,0,0,.45)}
.social{left:1127px;width:12px;height:12px;border-radius:50%;background:var(--navy)}
.about-bg{left:0;top:595px;width:1200px;height:358px;background:linear-gradient(100deg,#f7f7f7 0%,#e4e4e4 30%,#f6f6f6 60%,#ededed 100%)}
.about-card{left:532px;top:503px;width:525px;height:373px;background:var(--light)}
.about-card h2{position:absolute;left:36px;top:38px;font-size:44px;line-height:49px;font-weight:700;color:var(--navy)}
.about-card p{position:absolute;left:36px;top:146px;width:462px;font-size:13px;line-height:26px;letter-spacing:-0.2px}
.btn{display:block;background:var(--red);color:var(--white);font-size:14px;font-weight:600;text-align:center;text-transform:uppercase}
.about-card .btn{position:absolute;left:36px;top:294px;width:135px;height:41px;line-height:41px}
.services-band{left:0;top:953px;width:1200px;height:301px;background:var(--navy)}
.services-title{left:163px;top:1028px;font-size:42px;font-weight:700;color:var(--white)}
.services-lead{left:163px;top:1086px;width:540px;font-size:14px;line-height:27px;color:var(--white)}
.card-frame{width:265px;height:359px;border:2px solid var(--line);background:transparent}
.card{width:265px;height:359px;background:var(--light)}
.card svg{position:absolute;left:26px;top:38px}
.card h3{position:absolute;left:26px;top:108px;font-size:21px;font-weight:600;color:var(--navy);letter-spacing:-0.2px;white-space:nowrap}
.card p{position:absolute;left:26px;top:143px;width:226px;font-size:12px;line-height:21.7px;letter-spacing:-0.2px}
.card a{position:absolute;left:26px;top:311px;font-size:13px;font-weight:600;color:var(--red);text-decoration:underline}
.reviews-title{left:0;top:1624px;width:1200px;text-align:center;font-size:44px;font-weight:700;color:var(--navy)}
.review{width:421px;height:247px;background:var(--white);box-shadow:0 0 10px rgba(0,0,0,.12)}
.avatar{position:absolute;left:30px;top:28px;width:76px;height:76px;border-radius:50%}
.stars{position:absolute;left:130px;top:38px;color:var(--orange);font-size:17px;letter-spacing:2px}
.review h4{position:absolute;left:130px;top:70px;font-size:18px;font-weight:600;color:var(--red)}
.review p{position:absolute;left:31px;top:122px;width:360px;font-size:13px;line-height:24.6px;letter-spacing:-0.1px}
.dot{top:1982px;width:12px;height:12px;border-radius:50%;border:1px solid #bbb;background:#eee}
.dot.on{background:var(--red);border-color:var(--red)}
.cta{left:0;top:2069px;width:1200px;height:344px;background:linear-gradient(100deg,#34437c 0%,#5a6aa0 45%,#4c5c95 70%,#3b4a83 100%)}
.cta-title{left:0;top:2152px;width:1200px;text-align:center;color:var(--white);font-size:36px;font-weight:600;line-height:52px}
.cta-btn{left:510px;top:2278px;width:180px;height:42px;line-height:42px}
.foot-logo{left:0;top:2475px;width:1200px;text-align:center;font-size:44px;font-weight:700;color:var(--navy)}
.foot-nav{left:0;top:2568px;width:1200px;display:flex;justify-content:center;gap:40px;font-size:13px;text-transform:uppercase}
.rule{left:161px;width:878px;height:1px;background:var(--line)}
.contact-icon{width:54px;height:54px;border-radius:50%;background:var(--red)}
.contact-label{font-size:14px;font-weight:600;text-transform:uppercase}
.contact-value{font-size:14px;line-height:20px}
.copy{left:0;top:2757px;width:1200px;text-align:center;font-size:13px}
</style>
</head>
<body>
<header>
  <div class="abs logo">VELTRONA</div>
  <div class="abs nav active" style="left:563px">Home</div>
  <div class="abs nav" style="left:642px">About Us</div>
  <div class="abs nav" style="left:749px">Services</div>
  <div class="abs nav" style="left:851px">Reviews</div>
  <div class="abs nav" style="left:951px">Contact Us</div>
</header>

<section>
  <div class="abs hero" role="img" aria-label="Business people shaking hands in an office, blue tint"></div>
  <h1 class="abs hero-title">We Provide Business And<br>Consulting Services</h1>
  <span class="abs social" style="top:230px"></span>
  <span class="abs social" style="top:287px"></span>
  <span class="abs social" style="top:345px"></span>
</section>

<section>
  <div class="abs about-bg" role="img" aria-label="Faint light grey view of a tall office building"></div>
  <div class="abs about-card">
    <h2>ABOUT<br>VELTRONA</h2>
    <p>Lorem ipsum dolor sit amet, consectetuer adipiscing elit, se diam nonummy nibh euismod tincidunt ut laoreet dolore mag aliquam erat volutpat. Ut wisi enim ad minim veniam, nostrud exercitation ullamcorper suscipit lobortis nisl ut aliquip ex ea commodo dolar consequat duis autem vel eum iriure dolor hendrer.</p>
    <span class="btn">Read More</span>
  </div>
</section>

<section>
  <div class="abs services-band"></div>
  <h2 class="abs services-title">OUR SERVICES</h2>
  <p class="abs services-lead">Lorem ipsum dolor sit amet, consectetuer adipiscing elit, se diam nonummy nibh euismod tincidunt ut laoreet dolore mag aliquam erat volutpat.</p>

  <div class="abs card-frame" style="left:174px;top:1186px"></div>
  <div class="abs card-frame" style="left:472px;top:1186px"></div>
  <div class="abs card-frame" style="left:771px;top:1186px"></div>

  <div class="abs card" style="left:161px;top:1172px">
    <svg width="60" height="54" viewBox="0 0 60 54" fill="none" stroke="#1b2a6b" stroke-width="2">
      <path d="M4 22 L30 3 L56 22"/><path d="M9 19 V51 H51 V19"/><path d="M2 51 H58"/>
      <rect x="25" y="33" width="10" height="18" stroke="#d0111b"/><circle cx="30" cy="20" r="4" stroke="#d0111b"/>
      <rect x="13" y="32" width="8" height="8" stroke="#d0111b"/><rect x="39" y="32" width="8" height="8" stroke="#d0111b"/>
    </svg>
    <h3>Real Estate</h3>
    <p>Lorem ipsum dolor sit amet, cons ectetuer adipiscing elit, se diamw nonummy nibh euismod tincidunt ut laoreet dolore mag aliquam er volutpat. Ut wisi enim ad miniimn veniam, nostrud exercitation ullia mcorper suscipit lobortis.</p>
    <a>READ MORE</a>
  </div>

  <div class="abs card" style="left:459px;top:1172px">
    <svg width="56" height="54" viewBox="0 0 56 54" fill="none" stroke="#1b2a6b" stroke-width="2">
      <circle cx="28" cy="30" r="10" stroke="#d0111b"/><path d="M28 24 V36 M25 27 H31 M25 33 H31" stroke="#d0111b"/>
      <path d="M18 6 V16 M14 10 L18 6 L22 10 M38 6 V16 M34 10 L38 6 L42 10 M28 2 V12 M24 6 L28 2 L32 6" stroke="#d0111b"/>
      <path d="M4 28 C4 44 10 50 18 50 L22 42 L14 34 M52 28 C52 44 46 50 38 50 L34 42 L42 34"/>
    </svg>
    <h3>Wealth Management</h3>
    <p>Lorem ipsum dolor sit amet, cons ectetuer adipiscing elit, se diamw nonummy nibh euismod tincidunt ut laoreet dolore mag aliquam er volutpat. Ut wisi enim ad miniimn veniam, nostrud exercitation ullia mcorper suscipit lobortis.</p>
    <a>READ MORE</a>
  </div>

  <div class="abs card" style="left:758px;top:1172px">
    <svg width="56" height="54" viewBox="0 0 56 54" fill="none" stroke="#1b2a6b" stroke-width="2">
      <circle cx="28" cy="8" r="5" stroke="#d0111b"/><path d="M20 24 C20 16 36 16 36 24" stroke="#d0111b"/>
      <circle cx="9" cy="12" r="5"/><circle cx="47" cy="12" r="5"/>
      <path d="M3 52 V24 C3 18 15 18 15 24 V36 H20 V52 M53 52 V24 C53 18 41 18 41 24 V36 H36 V52"/>
      <path d="M16 28 H40"/><path d="M28 28 V52"/>
    </svg>
    <h3>Consulting</h3>
    <p>Lorem ipsum dolor sit amet, cons ectetuer adipiscing elit, se diamw nonummy nibh euismod tincidunt ut laoreet dolore mag aliquam er volutpat. Ut wisi enim ad miniimn veniam, nostrud exercitation ullia mcorper suscipit lobortis.</p>
    <a>READ MORE</a>
  </div>
</section>

<section>
  <h2 class="abs reviews-title">CLIENT REVIEWS</h2>
  <div class="abs review" style="left:161px;top:1702px">
    <div class="avatar" role="img" aria-label="Portrait photo of the client" style="background:#d9cfc6"></div>
    <div class="stars">★★★★★</div>
    <h4>Clara Whitmore</h4>
    <p>Lorem ipsum dolor sit amet, consectetuer adipiscing elit, sed diam nonummy nibh euismod tincidunt ut laoreet dolore magna aliquam erat volutpat. Ut wisi enim ad minim veniam, quis nostrud exercitation.</p>
  </div>
  <div class="abs review" style="left:618px;top:1702px">
    <div class="avatar" role="img" aria-label="Portrait photo of the client" style="background:#8a6a55"></div>
    <div class="stars">★★★★★</div>
    <h4>Darren Okafor</h4>
    <p>Lorem ipsum dolor sit amet, consectetuer adipiscing elit, sed diam nonummy nibh euismod tincidunt ut laoreet dolore magna aliquam erat volutpat. Ut wisi enim ad minim veniam, quis nostrud exercitation.</p>
  </div>
  <span class="abs dot on" style="left:574px"></span>
  <span class="abs dot" style="left:593px"></span>
  <span class="abs dot" style="left:613px"></span>
</section>

<section>
  <div class="abs cta" role="img" aria-label="Business people talking in a bright office, blue tint"></div>
  <h2 class="abs cta-title">Are You Looking For Professional Advice For<br>Your Business or Your Industry?</h2>
  <span class="abs btn cta-btn">Contact Us Today</span>
</section>

<footer>
  <div class="abs foot-logo">VELTRONA</div>
  <nav class="abs foot-nav">
    <span>Home</span><span>|</span><span>About Us</span><span>|</span><span>Services</span><span>|</span><span>Reviews</span><span>|</span><span>Contact Us</span>
  </nav>
  <div class="abs rule" style="top:2620px"></div>

  <div class="abs contact-icon" style="left:221px;top:2651px">
    <svg width="54" height="54" viewBox="0 0 54 54" fill="none" stroke="#fff" stroke-width="1.8"><path d="M19 16 L23 16 L25 22 L22 24 C24 28 26 30 30 32 L32 29 L38 31 V35 C38 37 36 38 34 38 C25 37 17 29 16 20 C16 18 17 16 19 16 Z"/></svg>
  </div>
  <div class="abs contact-label" style="left:288px;top:2657px">Phone</div>
  <div class="abs contact-value" style="left:288px;top:2681px">123-456-7890</div>

  <div class="abs contact-icon" style="left:466px;top:2651px">
    <svg width="54" height="54" viewBox="0 0 54 54" fill="none" stroke="#fff" stroke-width="1.8"><path d="M27 40 C21 33 18 28 18 23 A9 9 0 0 1 36 23 C36 28 33 33 27 40 Z"/><circle cx="27" cy="23" r="3.5"/></svg>
  </div>
  <div class="abs contact-label" style="left:533px;top:2649px">Address</div>
  <div class="abs contact-value" style="left:533px;top:2672px">123 Lorem ipsum dolor sit amet,<br>consectetuer adipiscing.</div>

  <div class="abs contact-icon" style="left:796px;top:2651px">
    <svg width="54" height="54" viewBox="0 0 54 54" fill="none" stroke="#fff" stroke-width="1.8"><rect x="16" y="20" width="22" height="16"/><path d="M16 20 L27 29 L38 20"/></svg>
  </div>
  <div class="abs contact-label" style="left:863px;top:2657px">Email</div>
  <div class="abs contact-value" style="left:863px;top:2679px">info@veltrona.com</div>

  <div class="abs rule" style="top:2733px"></div>
  <div class="abs copy">Copyright © 2020 <b>VELTRONA.</b> All Rights Reserved.</div>
</footer>
</body>
</html>
```